Health & Fitness Author & Public Speaker Needs Visually Stunning Web Design!

We've FINALLY got around to launching a website for Marisol Kettering - Australian Food Coach and Health & Fitness Expert. The website is to promote her new healthy eating program - "Bright Plate Living".
For a compehensive outline of exactly what we are after, please see the following attached files:
(1) Web Layout (wireframe, content/copy, links to photos to use, sample page we love)
(2) Style Guide (these are the colours, and overall feel we want)
Photos that we'd like used (of Marisol, and food/meals) can be found at these URL's:
Profile: https://www.filecrate.net/sh/q4r8vzkp2w7ttc3/H5M2xpLbeq
PixVault: https://www.filecrate.net/sh/b7mfwqjd3ue58an/9pq4Rtyhh2
HINT:
Before you do ANYTHING - check out this site as it is pretty much EXACTLY what we're after, but with our branding/colours/style: http://tovahlund.net/
As we will need to revamp our existing Chatterbook page & other printed material, there may be the potential for further work for the successful designer in the future.
Thanks & Good Luck!
Dorian Welch
Marketing & Business Development Manager
Bright Plate Living
Target Market(s)
Women, Ages 24 - 45, Interested in Healthly Eating & Fitness
Industry/Entity Type
Business
Look and feel
Each slider illustrates characteristics of the customer's brand and the style your logo design should communicate.

```html
<!DOCTYPE html>
<html lang="en">
<head>
<meta charset="utf-8">
<title>Bright Plate Living</title>
<link href="https://fonts.googleapis.com/css2?family=PT+Sans:wght@400;700&family=Open+Sans:wght@400;600&display=swap" rel="stylesheet">
<style>
:root{
  --pink:#e2175b;
  --pink-dark:#b80f47;
  --purple:#951fa3;
  --purple-btn:#7a1aa8;
  --ink:#2b2b2b;
  --muted:#666;
  --rule:#bdbdbd;
  --backdrop:#4a4a4a;
  --paper:#ffffff;
}
*{box-sizing:border-box;margin:0;padding:0}
html,body{width:921px;height:1200px;overflow:hidden}
body{background:var(--backdrop);font-family:"PT Sans",sans-serif;color:var(--ink);position:relative}
.page{position:absolute;left:79px;top:0;width:763px;height:1200px;background:var(--paper)}
.abs{position:absolute}

/* header */
.header{left:0;top:0;width:763px;height:94px;background:linear-gradient(#fff,#ececec)}
.brand{left:25px;top:30px;font-size:25px;font-weight:700;color:var(--pink);letter-spacing:-0.5px;line-height:1}
.nav{left:320px;top:42px;width:421px;height:28px;background:var(--pink);border-radius:2px;display:flex;align-items:center;box-shadow:0 1px 2px rgba(0,0,0,.3)}
.nav a{color:#fff;text-decoration:none;font-size:11px;height:28px;line-height:28px;padding:0 13px;border-right:1px solid var(--pink-dark)}
.nav a.current{background:var(--pink-dark);font-weight:700;width:54px;text-align:center}
.search{margin-left:auto;margin-right:4px;width:170px;height:20px;background:#fff;border-radius:2px;font-size:10px;color:#888;line-height:20px;padding-left:7px;position:relative}
.search svg{position:absolute;right:4px;top:3px}

/* hero */
.hero{left:0;top:94px;width:763px;height:272px;background:linear-gradient(100deg,#5a554f 0%,#7b746b 35%,#6a645c 60%,#4b4742 100%)}
.hero-photo{left:60px;top:0;width:330px;height:272px;background:linear-gradient(160deg,#8a6b58,#c39a85 45%,#d8cfc8 70%,#7c7167)}
.hero-copy{left:459px;top:60px;color:#fff;text-shadow:0 1px 3px rgba(0,0,0,.5)}
.hero-copy h1{font-size:21px;line-height:25px;font-weight:700;text-transform:uppercase}
.hero-copy p{font-size:14px;margin-top:2px;margin-left:3px}
.arrow{top:98px}
.dots{left:689px;top:252px;display:flex;gap:4px}
.dots span{width:10px;height:10px;border-radius:50%;background:#fff}
.dots span.on{background:var(--pink)}

/* signup band */
.join-band{left:0;top:366px;width:763px;height:82px;border-bottom:1px solid #ccc}
.join-band h2{position:absolute;left:21px;top:16px;font-size:18px;color:var(--purple);font-weight:700}
.join-band p{position:absolute;left:21px;top:39px;width:320px;text-align:center;font-size:10.5px;line-height:13px}
.field{height:22px;border:1px solid #aaa;border-radius:2px;font-family:"Open Sans",sans-serif;font-size:10px;color:#888;line-height:20px;padding-left:6px;background:#fff}
.btn{height:24px;border-radius:2px;color:#fff;font-weight:700;font-size:11px;text-align:center;line-height:24px;background:linear-gradient(var(--pink),var(--pink-dark));box-shadow:0 2px 2px rgba(0,0,0,.25)}
.btn.purple{background:linear-gradient(#8a22b8,#62138c)}
.band-shadow{left:60px;top:448px;width:640px;height:14px;background:radial-gradient(ellipse at top,rgba(0,0,0,.22),rgba(0,0,0,0) 70%)}

/* posts */
.post-title{font-size:17.5px;font-weight:700;color:var(--purple);line-height:18px}
.meta{display:flex;justify-content:space-between;font-family:"Open Sans",sans-serif;font-size:8.5px;color:var(--pink);padding:0 4px}
.dashed{height:0;border-top:1px dashed var(--rule)}
.photo{border:1px solid #ccc;padding:3px;background:#fff}
.photo div{width:100%;height:100%}
.excerpt{font-family:"Open Sans",sans-serif;font-size:8.6px;line-height:13.8px;color:#555}
.excerpt a{color:var(--pink);font-weight:600;text-decoration:none;margin-left:6px}

/* sidebar */
.side-head{left:491px;width:251px;height:26px;border-top:1px dashed var(--rule);border-bottom:1px dashed var(--rule);text-align:center;line-height:24px;font-size:12px;font-weight:700;color:var(--pink)}
.side-text{font-size:10.5px;line-height:16px}

/* footer */
.footer{left:0;top:1158px;width:763px;height:42px;background:var(--pink)}
.footer-links{position:absolute;left:15px;top:15px;font-size:8.5px;color:#fff;font-family:"Open Sans",sans-serif}
.footer-links span{margin:0 6px}
.social{position:absolute;right:14px;top:11px;display:flex;gap:8px}
.social span{font-size:9px;font-weight:700;color:#fff;line-height:20px}
</style>
</head>
<body>
<div class="page">

  <header class="abs header">
    <div class="abs brand">brightplate living</div>
    <nav class="abs nav">
      <a class="current">Home</a><a>About</a><a>The Plan</a><a>Shop</a>
      <div class="search">Search
        <svg width="14" height="14" viewBox="0 0 14 14"><circle cx="5.5" cy="5.5" r="4" fill="none" stroke="#e2175b" stroke-width="2"/><line x1="8.5" y1="8.5" x2="13" y2="13" stroke="#e2175b" stroke-width="2.4"/></svg>
      </div>
    </nav>
  </header>

  <section class="abs hero">
    <div class="abs hero-photo" role="img" aria-label="Smiling woman in a white crochet top against a weathered concrete wall"></div>
    <svg class="abs arrow" style="left:14px" width="14" height="60" viewBox="0 0 14 60"><polyline points="12,2 2,30 12,58" fill="none" stroke="#333" stroke-width="3"/></svg>
    <svg class="abs arrow" style="left:728px" width="14" height="60" viewBox="0 0 14 60"><polyline points="2,2 12,30 2,58" fill="none" stroke="#333" stroke-width="3"/></svg>
    <div class="abs hero-copy">
      <h1>Get slim<br>Boost energy<br>Guilt free<br>With Bright Plate Living!</h1>
      <p>With Marisol Kettering</p>
    </div>
    <div class="abs dots"><span class="on"></span><span></span><span></span><span></span></div>
  </section>

  <section class="abs join-band">
    <h2>Join the Bright Plate Living Movement!</h2>
    <p>Get a Weekly serving of Inspiration &amp; Advice that will change your life... Bring It On!</p>
    <div class="abs field" style="left:333px;top:32px;width:154px">Name</div>
    <div class="abs field" style="left:494px;top:32px;width:153px">Email</div>
    <div class="abs btn purple" style="left:654px;top:31px;width:88px">Hook Me Up</div>
  </section>
  <div class="abs band-shadow"></div>

  <!-- main post -->
  <article>
    <h2 class="abs post-title" style="left:21px;top:479px">Lorem Ipsum Dolor Sit Amet</h2>
    <div class="abs meta" style="left:21px;top:510px;width:436px"><span>January 19, 2013</span><span>112 Comments</span></div>
    <div class="abs dashed" style="left:21px;top:530px;width:436px"></div>
    <div class="abs photo" style="left:22px;top:549px;width:436px;height:157px">
      <div role="img" aria-label="Green kiwi smoothies beside a smiling woman" style="background:linear-gradient(90deg,#7fbf4a 0%,#a8d36b 22%,#e6e0d6 45%,#c9b8a8 70%,#e4ddd4 100%)"></div>
    </div>
    <p class="abs excerpt" style="left:22px;top:717px;width:436px">Lorem ipsum dolor sit amet, consectetur adipisicing elit, sed do eiusmod tempor incididunt ut labore et dolore magna aliqua. Ut enim ad minim veniam, quis nostrud exercitation ullamco laboris nisi ut aliquip ex ea commodo consequat. Duis aute irure dolor in reprehenderit in voluptate velit esse cillum dolore eu fugiat nulla pariatur. Excepteur sint occaecat cupidatat non proident, sunt in culpa qui officia deserunt mollit anim id est laborum. <a>Read more</a></p>
  </article>

  <article>
    <h2 class="abs post-title" style="left:21px;top:814px;width:210px">Sed ut Perspiciatis Unde Omnis Iste Natus</h2>
    <div class="abs meta" style="left:21px;top:861px;width:210px"><span>January 18, 2013</span><span>150 Comments</span></div>
    <div class="abs dashed" style="left:21px;top:880px;width:208px"></div>
    <div class="abs photo" style="left:20px;top:898px;width:206px;height:153px">
      <div role="img" aria-label="Wooden bowl of green apples, broccoli and kiwi" style="background:radial-gradient(ellipse at 50% 60%,#b8cf4a,#5f9a2e 55%,#2f5a22)"></div>
    </div>
    <p class="abs excerpt" style="left:20px;top:1060px;width:210px">Lorem ipsum dolor sit amet, consectetur adipisicing elit, sed do eiusmod tempor incididunt ut labore et dolore magna aliqua. Ut enim ad minim veniam, quis nostrud exercitation ullamco laboris nisi ut aliquip consequat. <a>Read more</a></p>
  </article>

  <article>
    <h2 class="abs post-title" style="left:251px;top:814px;width:215px">At Vero Eos et Accusamus Iusto Odio Dignissimos</h2>
    <div class="abs meta" style="left:251px;top:861px;width:210px"><span>January 17, 2013</span><span>150 Comments</span></div>
    <div class="abs dashed" style="left:251px;top:880px;width:208px"></div>
    <div class="abs photo" style="left:251px;top:898px;width:207px;height:153px">
      <div role="img" aria-label="Salad of rocket, avocado, mango and walnuts" style="background:radial-gradient(ellipse at 60% 55%,#f0a532,#9bc44a 50%,#5c8d2c)"></div>
    </div>
    <p class="abs excerpt" style="left:251px;top:1060px;width:210px">Lorem ipsum dolor sit amet, consectetur adipisicing elit, sed do eiusmod tempor incididunt ut labore et dolore magna aliqua. Ut enim ad minim veniam, quis nostrud exercitation ullamco laboris nisi ut aliquip consequat. <a>Read more</a></p>
  </article>

  <!-- sidebar -->
  <aside>
    <div class="abs side-head" style="top:482px">BRIGHT PLATE LIVING GUIDE</div>
    <div class="abs" role="img" aria-label="Tablet showing the Bright Plate Living Plan e-book cover" style="left:500px;top:522px;width:114px;height:158px;background:linear-gradient(160deg,#2a2a2a,#111);border-radius:8px;padding:8px 7px 16px">
      <div style="width:100%;height:100%;background:linear-gradient(#f4f0f4 0%,#f4e8f0 55%,#e86aa4 75%,#f4f0f4 100%)"></div>
    </div>
    <p class="abs side-text" style="left:629px;top:536px">The <b>ULTIMATE</b><br>Bright Plate<br>Living Guide</p>
    <div class="abs btn" style="left:629px;top:602px;width:101px;height:27px;line-height:27px">Get It Now!</div>

    <div class="abs side-head" style="top:722px">12 WEEK CHALLENGE</div>
    <div class="abs photo" style="left:500px;top:762px;width:117px;height:149px">
      <div role="img" aria-label="Smiling woman holding grapes against a stone wall" style="background:linear-gradient(170deg,#8f8579,#b7a898 45%,#d9d2cc 70%,#8a8177)"></div>
    </div>
    <p class="abs side-text" style="left:629px;top:778px"><b>HEALTHY,<br>HAPPY &amp; HOT</b><br>In No Time Flat!</p>
    <div class="abs btn" style="left:629px;top:837px;width:101px;height:27px;line-height:27px">Join Us Now!</div>

    <div class="abs side-head" style="top:948px">JOIN THE MOVEMENT!</div>
    <p class="abs" style="left:497px;top:985px;width:240px;text-align:center;font-family:'Open Sans',sans-serif;font-size:9.4px;line-height:16px">Join the Bright Plate Living Movement and get a free copy of The Kick Start Plan (valued $27.00)!</p>
    <div class="abs field" style="left:506px;top:1028px;width:213px">Name</div>
    <div class="abs field" style="left:506px;top:1061px;width:213px">Email</div>
    <div class="abs btn" style="left:567px;top:1098px;width:100px;height:28px;line-height:28px">Sign Me Up</div>
  </aside>

  <footer class="abs footer">
    <div class="footer-links">Community<span>|</span>Free<span>|</span>Resources<span>|</span>Press<span>|</span>Contact</div>
    <div class="social"><span>Chatterbook</span><span>Chirpline</span><span>Clipstream</span></div>
  </footer>
</div>
</body>
</html>
```